Harrowgate Estates Business Card for Apartment Buildings

Create business cards for resident managers who run apartment buildings. The audience is the public who are searching for apartment rentals, and current residents who live at the apartment building. Key design element will be incorporating the company logo, however, the logo cannot dominate. The building name and manager name are more important than the logo. Current business card design leaves little room for copy, so we may need to reduce the size on the current card to allow for more space for copy.

Target Market(s)

Adults 18-65 years of age, who are looking for an apartment rental, plus current residents who live at our apartment buildings.

Industry/Entity Type

Property Management

Contact Information for Business Card

A major design element will be use of the company logo. Important property and manager contact information must be part of the design. The size of the logo will need to be reduced to make room for building and manager contact copy.

Font styles to use
Sans Serif

Colors
3176b5
000000
959595
ffffff

Requirements
Must have
• 1) Incorporate the company logo.
• 2) Use the company colors (dark blue, black/grey, over white).
• 3) FEATURE THE BUILDING NAME
• 4) FEATURE THE MANAGER NAME
• 5) The company name is less important than BUILDING and MANAGER
• 6) Manager contact information
• **SEE ATTACHED CREATIVE BRIEF**
Nice to have
• 1) Back of card logo watermark
• 2) Ability to write notes on back of carfd
Should not have
• Avoid letting the company logo dominate the card, the building name and manager are more important than the company logo.

```html
<!DOCTYPE html>
<html lang="en">
<head>
<meta charset="utf-8">
<title>Harrowgate Estates – Resident Manager Card</title>
<link rel="stylesheet" href="https://fonts.googleapis.com/css2?family=Montserrat:wght@400;500;600;700;800&display=swap">
<style>
  :root {
    --brand-blue: #0f5b9a;
    --accent-blue: #3176b5;
    --ink: #000000;
    --ink-soft: #1c1c1c;
    --grey: #959595;
    --grey-light: #e4e6e9;
    --paper: #ffffff;
    --backdrop: #eceef1;
  }
  * { box-sizing: border-box; margin: 0; padding: 0; }
  html, body {
    width: 1200px; height: 900px; overflow: hidden;
    background: var(--backdrop);
    font-family: "Montserrat", sans-serif;
  }
  .canvas { position: relative; width: 1200px; height: 900px; }
  .card {
    position: absolute; width: 700px; height: 400px;
    background: var(--paper); overflow: hidden;
    box-shadow: 0 6px 20px rgba(0,0,0,0.18);
  }
  .card--back { left: 170px; top: 30px; }
  .card--front { left: 330px; top: 470px; }

  .wordmark { display: flex; align-items: center; gap: 8px; }
  .wordmark__square { width: 22px; height: 22px; background: var(--brand-blue); }
  .wordmark__name {
    color: var(--brand-blue); font-weight: 700; font-size: 17px;
    letter-spacing: 0.04em; text-transform: uppercase; line-height: 1;
  }

  /* back */
  .card--back .wordmark { position: absolute; left: 40px; top: 52px; }
  .watermark { position: absolute; right: -120px; top: -70px; width: 460px; height: 460px; }
  .notes { position: absolute; left: 60px; top: 120px; width: 330px; }
  .notes__line { height: 42px; border-bottom: 1.5px dotted var(--grey); }

  /* front */
  .accent-block { position: absolute; left: 0; top: 120px; width: 28px; height: 48px; background: var(--brand-blue); }
  .manager { position: absolute; left: 62px; top: 86px; }
  .manager__name { color: var(--brand-blue); font-weight: 800; font-size: 21px; letter-spacing: 0.03em; text-transform: uppercase; }
  .manager__title { color: var(--ink); font-weight: 700; font-size: 17px; margin-top: 2px; }
  .contact { position: absolute; left: 62px; list-style: none; }
  .contact--phones { top: 196px; }
  .contact--web { top: 268px; }
  .contact__item { display: flex; align-items: center; gap: 9px; font-size: 17px; color: var(--ink-soft); line-height: 23px; font-weight: 500; }
  .contact__icon { width: 15px; height: 15px; flex: none; }
  .band { position: absolute; left: 0; bottom: 0; width: 540px; height: 112px; }
  .property { position: absolute; left: 62px; bottom: 20px; color: var(--paper); }
  .property__name { font-weight: 800; font-size: 19px; letter-spacing: 0.03em; text-transform: uppercase; margin-bottom: 4px; }
  .property__line { font-size: 17px; font-weight: 400; line-height: 21px; }
  .card--front .wordmark { position: absolute; left: 480px; top: 268px; }
</style>
</head>
<body>
<main class="canvas">

  <section class="card card--back" aria-label="Card back with notes area">
    <svg class="watermark" viewBox="0 0 460 460" aria-hidden="true">
      <circle cx="230" cy="230" r="200" fill="none" stroke="var(--grey-light)" stroke-width="34"/>
    </svg>
    <div class="wordmark">
      <span class="wordmark__square"></span>
      <span class="wordmark__name">Harrowgate Estates</span>
    </div>
    <div class="notes">
      <div class="notes__line"></div>
      <div class="notes__line"></div>
      <div class="notes__line"></div>
      <div class="notes__line"></div>
      <div class="notes__line"></div>
      <div class="notes__line"></div>
    </div>
  </section>

  <section class="card card--front" aria-label="Card front">
    <div class="accent-block"></div>
    <div class="manager">
      <p class="manager__name">Marisol Delgado</p>
      <p class="manager__title">Resident Manager</p>
    </div>

    <ul class="contact contact--phones">
      <li class="contact__item">
        <svg class="contact__icon" viewBox="0 0 16 16" aria-hidden="true"><circle cx="8" cy="8" r="8" fill="var(--brand-blue)"/><path d="M4 7.5c1-2 7-2 8 0l-1.2 1-1.3-.8v-1h-3v1l-1.3.8z" fill="var(--paper)"/></svg>
        555 014 2210
      </li>
      <li class="contact__item">
        <svg class="contact__icon" viewBox="0 0 16 16" aria-hidden="true"><circle cx="8" cy="8" r="8" fill="var(--brand-blue)"/><rect x="4" y="6" width="8" height="5" rx="1" fill="var(--paper)"/><rect x="6" y="4" width="4" height="2" fill="var(--paper)"/></svg>
        555 014 3387
      </li>
      <li class="contact__item">
        <svg class="contact__icon" viewBox="0 0 16 16" aria-hidden="true"><circle cx="8" cy="8" r="8" fill="var(--brand-blue)"/><rect x="5.5" y="3.5" width="5" height="9" rx="1" fill="none" stroke="var(--paper)" stroke-width="1.3"/></svg>
        555 014 7450
      </li>
    </ul>

    <ul class="contact contact--web">
      <li class="contact__item">
        <svg class="contact__icon" viewBox="0 0 16 16" aria-hidden="true"><circle cx="8" cy="8" r="8" fill="var(--brand-blue)"/><rect x="4" y="5" width="8" height="6" fill="var(--paper)"/><path d="M4 5l4 3 4-3" fill="none" stroke="var(--brand-blue)" stroke-width="1"/></svg>
        marisol@harrowgate.com
      </li>
      <li class="contact__item">
        <svg class="contact__icon" viewBox="0 0 16 16" aria-hidden="true"><circle cx="8" cy="8" r="8" fill="var(--brand-blue)"/><circle cx="8" cy="8" r="4.5" fill="none" stroke="var(--paper)" stroke-width="1"/><path d="M3.5 8h9M8 3.5c-2 2.5-2 6.5 0 9M8 3.5c2 2.5 2 6.5 0 9" fill="none" stroke="var(--paper)" stroke-width="0.9"/></svg>
        www.harrowgate.com
      </li>
    </ul>

    <svg class="band" viewBox="0 0 540 112" preserveAspectRatio="none" aria-hidden="true">
      <path d="M0 0H455Q470 0 480 14L540 112H0Z" fill="var(--brand-blue)"/>
    </svg>
    <div class="property">
      <p class="property__name">Cedar Ridge Apartments</p>
      <p class="property__line">2418 Linden Avenue</p>
      <p class="property__line">Fairview, CA 90210</p>
    </div>

    <div class="wordmark">
      <span class="wordmark__square"></span>
      <span class="wordmark__name">Harrowgate Estates</span>
    </div>
  </section>

</main>
</body>
</html>
```